Business Card Design

We need a design that will also transfer to car decals
We need a design that will speak to the average person needing home and office remodeling
The design should be fresh, exciting, easy to read in a glance and unique
We would like a die-cut tool belt
Bright colors and evenly spaced information

Target Market(s)

Home and business owners
Middle and Upper Income property owners
Families and people with fixer upper homes

Industry/Entity Type

Business

Contact Information for Business Card

Looking for the best Bay Area Handyman? Here I am!
RKW Handyman Services does it all at prices regular people can afford.
Electrical, Plumbing, Carpentry, Remodeling, Fencing, Picture and window placement, Hauling ... and anything else you can imagine!
510-473-2918
Serving the Entire Bay Area
Free Estimates! Call us Today to turn your dreams into reality!

Font styles to use
Serif

Requirements
Must have
• Speaks to the average person
stands out among similar industry cards
Nice to have
• fun, comical, you want to hold on to this card
Should not have
• bland colors
look too crowded

```html
<!DOCTYPE html>
<html lang="en">
<head>
<meta charset="utf-8">
<title>RKW Handyman Services – Business Card</title>
<link href="https://fonts.googleapis.com/css2?family=Arimo:wght@400;700&display=swap" rel="stylesheet">
<style>
  :root {
    --backdrop: #e4e4e4;
    --card-dark: #231f20;
    --accent-green: #8cc63f;
    --accent-orange: #f7941d;
    --text-light: #ffffff;
    --text-dark: #1a1a1a;
    --tool-tone: rgba(95, 91, 92, 0.45);
    --tool-fade: rgba(95, 91, 92, 0);
  }
  html, body {
    margin: 0;
    width: 1200px;
    height: 900px;
    overflow: hidden;
    background: var(--backdrop);
    font-family: "Arimo", Arial, sans-serif;
  }
  .stage {
    position: relative;
    width: 1200px;
    height: 900px;
    display: flex;
    align-items: center;
    justify-content: center;
  }
  .card {
    position: relative;
    width: 940px;
    height: 520px;
    border-radius: 34px;
    overflow: hidden;
    display: flex;
    background: var(--card-dark);
    box-shadow: 0 10px 30px rgba(0,0,0,0.25);
  }
  .card-main {
    position: relative;
    width: 610px;
    height: 100%;
    color: var(--text-light);
    text-align: center;
  }
  .tool-art {
    position: absolute;
    left: 40px;
    top: 200px;
    width: 340px;
    height: 320px;
    border-radius: 40px;
    background: radial-gradient(ellipse at 50% 55%, var(--tool-tone) 0%, var(--tool-fade) 70%);
  }
  .card-content {
    position: relative;
    padding: 58px 30px 0 50px;
  }
  .tagline {
    font-size: 23px;
    line-height: 1.25;
    margin: 0;
  }
  .company-name {
    font-size: 38px;
    color: var(--accent-orange);
    margin: 18px 0 2px;
    font-weight: 400;
    letter-spacing: 0.5px;
  }
  .company-promise {
    font-size: 19px;
    margin: 0;
  }
  .call-line {
    font-size: 19px;
    line-height: 1.2;
    margin: 46px 0 0;
    text-transform: uppercase;
  }
  .phone {
    font-size: 66px;
    margin: 4px 0 0;
    letter-spacing: 1px;
  }
  .service-area {
    position: absolute;
    left: 0;
    right: 0;
    bottom: 38px;
    font-size: 19px;
    text-transform: uppercase;
    margin: 0;
  }
  .divider {
    width: 7px;
    height: 100%;
    background: var(--accent-orange);
  }
  .card-services {
    flex: 1;
    background: var(--accent-green);
    padding: 44px 24px 0 30px;
    color: var(--text-dark);
  }
  .service-list {
    list-style: none;
    margin: 0;
    padding: 0;
  }
  .service-list li {
    display: flex;
    align-items: center;
    font-size: 19px;
    text-transform: uppercase;
    letter-spacing: 0.5px;
    margin-bottom: 18px;
  }
  .service-list li::before {
    content: "";
    width: 12px;
    height: 12px;
    border-radius: 50%;
    background: var(--text-dark);
    margin-right: 12px;
    flex: none;
  }
  .service-extra {
    font-size: 19px;
    text-transform: uppercase;
    line-height: 1.2;
    margin: 0 0 0 24px;
  }
</style>
</head>
<body>
<main class="stage">
  <article class="card">
    <section class="card-main">
      <div class="tool-art" role="img" aria-label="Faint hammer watermark illustration"></div>
      <div class="card-content">
        <p class="tagline">Looking for the best Bay Area Handyman?<br>Here I am!</p>
        <h1 class="company-name">RKW HANDYMAN SERVICES</h1>
        <p class="company-promise">Does it all at prices regular people can afford</p>
        <p class="call-line">Call us today<br>to turn your dreams into reality!</p>
        <p class="phone">510-473-2918</p>
      </div>
      <p class="service-area">Serving the entire Bay Area free estimates!</p>
    </section>
    <div class="divider"></div>
    <section class="card-services">
      <ul class="service-list">
        <li>Electrical</li>
        <li>Plumbing</li>
        <li>Carpentry</li>
        <li>Remodeling</li>
        <li>Fencing</li>
        <li>Picture placement</li>
        <li>Window placement</li>
        <li>Hauling …</li>
      </ul>
      <p class="service-extra">And anything else<br>you can imagine!</p>
    </section>
  </article>
</main>
</body>
</html>
```